It's a new electrical company based in Newcastle NSW. I would like a logo between the two words "BRYN (insert logo) VOLT". I would like the logo to represent electrical and celtic style. For example I have seen a light bulb with a celtic pattern in the middle which looked very good. I would like it to be a white card, mainly black writing and quite basic not too much going on. But maybe have the logo partially red or green?

BRYN VOLT
Electrical Contractors
Domestic, commercial, fault finding, testing, re wires, switchboard upgrades
License No: 738421K
Fully Insured
Phone: 0431587720

```html
<!DOCTYPE html>
<html lang="en">
<head>
<meta charset="utf-8">
<title>BRYN VOLT Electrical Contractors – Business Card</title>
<link href="https://fonts.googleapis.com/css2?family=Cinzel:wght@400&family=EB+Garamond:wght@400&display=swap" rel="stylesheet">
<style>
  :root {
    --paper: #ffffff;
    --ink: #111111;
    --brand-red: #e8252b;
    --frame-blue: #1fb0e6;
  }
  html, body {
    margin: 0;
    padding: 0;
    width: 1200px;
    height: 567px;
    overflow: hidden;
    background: var(--paper);
  }
  .canvas {
    position: relative;
    width: 1200px;
    height: 567px;
    background: var(--paper);
    font-family: "EB Garamond", "Times New Roman", serif;
    color: var(--ink);
  }
  .card {
    position: absolute;
    left: 234px;
    top: 6px;
    width: 942px;
    height: 549px;
    border: 4px solid var(--frame-blue);
    background: var(--paper);
  }
  .brand-word {
    position: absolute;
    top: 128px;
    margin: 0;
    font-family: "Cinzel", "Times New Roman", serif;
    font-weight: 400;
    font-size: 84px;
    line-height: 1;
    color: var(--brand-red);
    letter-spacing: 2px;
  }
  .brand-word--first { right: 590px; }
  .brand-word--second { left: 764px; }
  .brand-mark {
    position: absolute;
    left: 643px;
    top: 118px;
    width: 108px;
    height: 108px;
  }
  .company-title {
    position: absolute;
    left: 234px;
    width: 950px;
    top: 278px;
    margin: 0;
    text-align: center;
    font-weight: 400;
    font-size: 41px;
    line-height: 1;
    letter-spacing: 0.5px;
  }
  .info {
    position: absolute;
    top: 392px;
    margin: 0;
    padding: 0;
    list-style: none;
    font-size: 27px;
    line-height: 36px;
  }
  .info--services { left: 261px; }
  .info--contact { left: 902px; }
</style>
</head>
<body>
  <main class="canvas">
    <section class="card" aria-label="BRYN VOLT business card"></section>

    <h1 class="brand-word brand-word--first">BRYN</h1>
    <svg class="brand-mark" viewBox="0 0 108 108" aria-hidden="true">
      <circle cx="54" cy="54" r="50" fill="none" stroke="var(--ink)" stroke-width="2"/>
    </svg>
    <span class="brand-word brand-word--second">VOLT</span>

    <h2 class="company-title">BRYN VOLT Electrical Contractors</h2>

    <ul class="info info--services">
      <li>Domestic &amp; Commercial fault finding</li>
      <li>Testing</li>
      <li>Rewires</li>
      <li>Switchboard upgrades</li>
    </ul>

    <ul class="info info--contact">
      <li>License No:738421K</li>
      <li>Fully Insured</li>
      <li>Phone:0431587720</li>
    </ul>
  </main>
</body>
</html>
```